Web site for small printshop

I am looking for a website for small printshop in Iceland, mainly serving university students and artist.

We print posters, flyers, business cards and more.

In addition to our current website, I would like to include design tool, (fx. www.quarlitune.example, www.dravonpix.example or something similar) jobs upload, shopping chart.
Updates

Great work, I am really amazed of the quality of work i am seeing here.

Really way beyond my expectation

GOOD JOB - all of you ! 

Hi all.

The designs submitted have been great, way better than expected.
I really did not expect this level of quality.

Some have been asking me for feedback on their designs, and I will try 
to send some feedback here, without spoiling your creativity.

Likes:
- when the colors of my logo is used in menus, buttons etc.
- simple, not to crowded look.

Dislikes.
- Dark and heavy design
- Lot of text and buttons (crowded look)

Extra info.
- top line (before menus) will contain: Tel - email - language
- menu line will have 5 categories: Home - service - submission of works - FAQ - about us
- 3 large buttons:  Job submit - Job design - ask for offer

LOVE YOUR WORK - great designs so far :)

Target Market(s)

University Students, Artists. Age group 20-30

Industry/Entity Type

University

Requirements
Must have
• The website must be easy to use, clean looking.

```html
<!DOCTYPE html>
<html lang="en">
<head>
<meta charset="utf-8">
<title>Prentvík — Print Shop</title>
<link href="https://fonts.googleapis.com/css2?family=Arimo:wght@400;700&display=swap" rel="stylesheet">
<style>
:root{
  --paper:#f1f0ea;
  --yellow-top:#f3dc55;
  --yellow-bottom:#fae463;
  --ink:#1d1d1b;
  --red:#e8352f;
  --green:#146b35;
  --rule:#dcdbd3;
  --card:#ffffff;
  --hero-light:#e6ebee;
  --hero-mid:#c9d6dd;
}
*{margin:0;padding:0;box-sizing:border-box}
html,body{width:882px;height:1200px;overflow:hidden}
body{background:var(--paper);font-family:"Arimo",Arial,sans-serif;color:var(--ink);position:relative}
.abs{position:absolute}

.site-header{position:absolute;left:0;top:0;width:882px;height:76px;background:linear-gradient(180deg,var(--yellow-top),var(--yellow-bottom))}
.brand{position:absolute;left:73px;top:27px;display:flex;align-items:center;gap:8px}
.brand-mark{width:22px;height:22px;background:var(--red)}
.brand-name{font-weight:700;font-size:18px;letter-spacing:.3px;color:var(--ink)}
.main-nav a{position:absolute;top:35px;font-weight:700;font-size:15.5px;color:var(--ink);text-decoration:none}
.nav-active-bar{position:absolute;left:279px;top:76px;width:99px;height:8px;background:var(--green)}

.hero{position:absolute;left:0;top:76px;width:882px;height:270px;background:linear-gradient(90deg,var(--hero-mid) 0%,var(--hero-light) 25%,#eef0ef 70%,var(--paper) 100%)}
.hero-art{position:absolute;left:185px;top:8px;width:450px;height:255px;border-radius:40% 55% 45% 50%;background:radial-gradient(ellipse at 40% 40%,#3dc3cb 0%,#9fd8dc 35%,#e1e5e6 65%,rgba(230,235,238,0) 80%)}
.hero-title{position:absolute;left:605px;top:200px;font-weight:400;line-height:1}
.hero-title .l1{font-size:29px;color:var(--red)}
.hero-title .l1 b{font-weight:400;color:var(--green)}
.hero-title .l2{margin-top:2px;font-size:29px;color:var(--red);padding-left:52px}
.hero-title .l2 small{font-size:15px;color:var(--ink);margin-right:4px}

.sub-nav{position:absolute;top:367px;left:0;width:882px;font-size:13px;font-weight:400}
.sub-nav span{position:absolute;top:0}
.rule{position:absolute;left:131px;width:584px;height:1px;background:var(--rule)}

.section-title{position:absolute;font-size:18px;font-weight:400;color:var(--ink)}
.section-heading{position:absolute;left:0;width:882px;text-align:center;font-size:18px;color:var(--green)}
.body-copy{position:absolute;font-size:9px;line-height:15.5px;color:var(--ink)}

.placeholder-photo{position:absolute}

.step-u{position:absolute;left:166px;top:690px;font-size:54px;color:var(--red);line-height:1}
.step-label{position:absolute;font-size:12.5px;font-weight:700}
.step-sub{position:absolute;font-family:"Times New Roman",serif;font-size:8px;color:#666;letter-spacing:.3px}
.select-title{position:absolute;left:327px;top:690px;font-size:18px}
.select-title em{font-style:normal;font-size:13px;color:var(--red)}
.size-select{position:absolute;left:326px;top:717px;width:142px;height:30px;background:#f7f7f4;border:1px solid #cfcfca;font-size:10px;display:flex;align-items:center;justify-content:center}
.size-select svg{position:absolute;right:10px;top:10px}
.pay-label{position:absolute;left:513px;top:733px;font-size:12px}

.printer-card-corner{position:absolute;width:53px;height:58px}
.printer-card{position:absolute;left:152px;top:866px;width:578px;height:202px;background:var(--card);box-shadow:0 1px 4px rgba(0,0,0,.08)}

.site-footer{position:absolute;top:1159px;left:0;width:882px;text-align:center;font-size:7px;font-weight:700}
.site-footer span{color:var(--red)}
</style>
</head>
<body>

<header class="site-header">
  <div class="brand"><div class="brand-mark"></div><span class="brand-name">PRENTVÍK</span></div>
  <nav class="main-nav">
    <a style="left:306px" href="#">HOME</a>
    <a style="left:403px" href="#">ABOUT US</a>
    <a style="left:513px" href="#">PORTOFOLIO</a>
    <a style="left:644px" href="#">CONTACT US</a>
  </nav>
</header>
<div class="nav-active-bar"></div>

<section class="hero">
  <div class="hero-art" role="img" aria-label="Photo of a jumping young man in a plaid shirt with splashes of turquoise, white and orange paint"></div>
  <h1 class="hero-title">
    <div class="l1">WORLD <b>OF</b></div>
    <div class="l2"><small>REAL</small>COLORS</div>
  </h1>
</section>

<nav class="sub-nav">
  <svg class="abs" style="left:170px;top:-4px" width="19" height="18" viewBox="0 0 19 18" aria-hidden="true">
    <path d="M9.5 1 L18 9 H15.5 V17 H11.5 V12 H7.5 V17 H3.5 V9 H1 Z" fill="var(--red)"/>
  </svg>
  <span style="left:207px">HOME</span>
  <span style="left:300px">CATOGOREY</span>
  <span style="left:452px">ABOUT US</span>
  <span style="left:574px">BUY ONLINE</span>
</nav>
<div class="rule" style="top:401px"></div>

<h2 class="section-title" style="left:131px;top:420px">STORY BOARD</h2>
<div class="placeholder-photo" role="img" aria-label="Tilted photo print icon showing a paintbrush with orange paint" style="left:192px;top:450px;width:92px;height:100px;background:linear-gradient(135deg,#d8d8d8,#4a4a4a 55%,#c7702a);transform:rotate(-14deg)"></div>
<p class="body-copy" style="left:315px;top:462px;width:375px">Malt Corner sprouted from a hot dog cart in Linden Row Park in Eastbrook created by Tobias Wren's Harbor Lane Kitchen Group (HLKG) to support the Linden Row Park Trust's first art installation. The cart was quite the success, with Corner Fans lined up daily for three summers.</p>

<div class="rule" style="top:566px"></div>
<h2 class="section-heading" style="top:587px">HOW CAN YOU CONTACT US</h2>
<div class="rule" style="top:625px"></div>

<div class="step-u">U</div>
<div class="step-label" style="left:218px;top:694px">PLOAD</div>
<div class="step-sub" style="left:218px;top:707px">YOUR FILES</div>
<svg class="abs" style="left:238px;top:716px" width="74" height="34" viewBox="0 0 74 34" aria-hidden="true">
  <rect x="2" y="12" width="4" height="11" fill="var(--ink)"/>
  <rect x="9" y="12" width="4" height="11" fill="var(--ink)"/>
  <rect x="16" y="12" width="4" height="11" fill="var(--ink)"/>
  <path d="M24 11 H40 V2 L72 17 L40 32 V23 H24 Z" fill="none" stroke="var(--ink)" stroke-width="3" stroke-linejoin="round"/>
</svg>

<div class="select-title">SELECT <em>THE SIZE</em></div>
<div class="size-select">A3
  <svg width="10" height="8" viewBox="0 0 10 8" aria-hidden="true"><path d="M1 2 L5 6 L9 2" fill="none" stroke="#333" stroke-width="1.6"/></svg>
</div>

<svg class="abs" style="left:483px;top:693px" width="44" height="22" viewBox="0 0 44 22" aria-hidden="true">
  <rect x="1" y="7" width="3" height="8" fill="var(--ink)"/>
  <rect x="6" y="7" width="3" height="8" fill="var(--ink)"/>
  <rect x="11" y="7" width="3" height="8" fill="var(--ink)"/>
  <path d="M16 7 H25 V1 L42 11 L25 21 V15 H16 Z" fill="none" stroke="var(--ink)" stroke-width="2" stroke-linejoin="round"/>
</svg>

<svg class="abs" style="left:647px;top:675px" width="46" height="46" viewBox="0 0 46 46" aria-hidden="true">
  <circle cx="23" cy="23" r="22" fill="var(--red)"/>
  <circle cx="23" cy="23" r="15" fill="none" stroke="#fff" stroke-width="1.5"/>
  <path d="M15 23 L21 29 L31 16" fill="none" stroke="#fff" stroke-width="4" stroke-linecap="round" stroke-linejoin="round"/>
</svg>
<div class="pay-label">AND PAY THE LOWEST COST</div>

<div class="rule" style="top:790px"></div>
<h2 class="section-heading" style="top:812px">3: OUR SELECTING USED PRINTER</h2>

<div class="printer-card-corner" style="left:137px;top:850px;background:var(--ink)"></div>
<div class="printer-card-corner" style="left:692px;top:1025px;background:var(--red)"></div>
<article class="printer-card">
  <div class="placeholder-photo" role="img" aria-label="Photo of a blue and black inkjet printer with paper" style="left:33px;top:27px;width:155px;height:150px;background:linear-gradient(160deg,#dfe3e6 0%,#3a8fd6 45%,#2a2d33 80%);border-radius:10px"></div>
  <h3 class="section-title" style="left:217px;top:40px">STORY BOARD</h3>
  <p class="body-copy" style="left:215px;top:82px;width:325px">Malt Corner sprouted from a hot dog cart in Linden Row Park in Eastbrook created by Tobias Wren's Harbor Lane Kitchen Group (HLKG) to support the Linden Row Park Trust's first art installation. The cart was quite the success, with Corner Fans lined up daily for three summers.</p>
</article>

<div class="rule" style="top:1141px;left:352px;width:200px"></div>
<footer class="site-footer">ALLRIGHTS RESERVED BY <span>COMPANY NAME</span>@THE DATE</footer>

</body>
</html>
```